Biz Card Design TPVC

New business card for a new company.
Logo was completed by a designer on ArtFlock and looking to continue requesting additional services.
Company Name: Tidal Prime Voltage Collective
Although this company is starting in Canada, we will be moving towards a global presence within the next 6 months.
Key elements to this business are as follows.
Energy Procurement
Energy Reduction Services
Demand Side Consulting
Energy Efficiency Consulting
Saving Clients Money
Helping Them Go "Green"
Managing Their Energy Requirements
Basically the goal for our company is to find the best procurement solution for our clients and reduce their energy consumption. This reduces their expenses and the amount of greenhouse gas they produce on a daily basis.
I have been in the energy footprint for the last 20 years and know that most companies are looking to "do whatever is necessary to get them to sign on the dotted line". I would prefer to walk away from a client that I can't help than to put them into a situation that they will regret for years to come. This is where the "TIDAL" part of the company name comes from.
The following is a catch phrase that encompasses what we do.
"Reducing your carbon footprint & energy bill at the same time!"
The back of the card needs to have this statement along with some sort of illustration. The back is a playground for creative ideas.
The front of the card needs the following.
Logo.
First & Last Name (Gus Marwick)
Title (Energy Warrior)
Phone Number (555) 314-2768
Fax Number (555) 862-4091
Email Address gus@tidalprimevoltage.example
Address 47 Orchard Lane Toronto Ontario K4P 2Z7
I want it to be a card that is remembered when any of my staff give it to a customer. It HAS to stand out.
Target Market(s)
Business Owners, Decision Makers, 30 to 65+
Industry/Entity Type
Business
Look and feel
Each slider illustrates characteristics of the customer's brand and the style your logo design should communicate.

```html
<!DOCTYPE html>
<html lang="en">
<head>
<meta charset="utf-8">
<title>Tidal Prime Voltage Collective – Business Card</title>
<link rel="stylesheet" href="https://fonts.googleapis.com/css2?family=Exo+2:wght@600&family=Arimo:wght@400;700&display=swap">
<style>
  :root {
    --bg: #d9d9d9;
    --card-black: #0b0b0b;
    --card-white: #ffffff;
    --brand-blue: #3b6fc6;
    --brand-green: #2fae4e;
    --leaf-green: #5cc466;
    --leaf-light: #9ee29a;
    --text-light: #f2f2f2;
  }
  * { box-sizing: border-box; margin: 0; padding: 0; }
  html, body { width: 1200px; height: 900px; overflow: hidden; }
  body {
    background: var(--bg);
    font-family: "Arimo", Arial, sans-serif;
    display: flex;
    flex-direction: column;
    align-items: center;
    justify-content: center;
    gap: 56px;
  }
  .card {
    width: 580px;
    height: 332px;
    position: relative;
    overflow: hidden;
    box-shadow: 0 6px 18px rgba(0,0,0,0.18);
  }

  /* Back */
  .card-back { background: var(--card-black); }
  .back-pattern {
    position: absolute;
    inset: 0;
    background:
      radial-gradient(ellipse 150px 110px at 300px 118px, rgba(92,196,102,0.55), rgba(92,196,102,0.18) 60%, rgba(92,196,102,0) 100%),
      radial-gradient(ellipse 230px 170px at 110px 250px, rgba(255,255,255,0.05), rgba(255,255,255,0) 100%),
      radial-gradient(ellipse 200px 160px at 470px 70px, rgba(255,255,255,0.05), rgba(255,255,255,0) 100%);
  }
  .back-content {
    position: absolute;
    left: 0; right: 0;
    top: 218px;
    display: flex;
    flex-direction: column;
    align-items: center;
    gap: 10px;
  }
  .brand {
    display: flex;
    align-items: center;
    gap: 12px;
  }
  .brand-dot {
    border-radius: 50%;
    background: var(--leaf-green);
    flex: none;
  }
  .brand-name {
    font-family: "Exo 2", "Arimo", sans-serif;
    font-weight: 600;
    color: var(--brand-blue);
    white-space: nowrap;
    letter-spacing: -0.3px;
  }
  .card-back .brand-dot { width: 34px; height: 34px; }
  .card-back .brand-name { font-size: 31px; }
  .tagline {
    color: var(--text-light);
    font-size: 14px;
  }

  /* Front */
  .card-front { background: var(--card-black); }
  .front-top {
    background: var(--card-white);
    height: 196px;
    display: flex;
    align-items: center;
    justify-content: center;
  }
  .card-front .brand-dot { width: 28px; height: 28px; }
  .card-front .brand-name { font-size: 26px; }
  .front-bottom {
    display: flex;
    justify-content: space-between;
    padding: 20px 26px 0 26px;
  }
  .person-name {
    color: var(--brand-green);
    font-size: 20px;
    font-weight: 700;
  }
  .person-title {
    color: var(--text-light);
    font-size: 11px;
    margin-top: 3px;
  }
  .person-address {
    color: var(--text-light);
    font-size: 12px;
    margin-top: 10px;
  }
  .contact-list {
    list-style: none;
    color: var(--text-light);
    font-size: 11px;
    line-height: 1.55;
  }
  .contact-label { font-weight: 700; margin-right: 4px; }
  .label-green { color: var(--brand-green); }
  .label-blue { color: var(--brand-blue); }
  .edge-stripe {
    position: absolute;
    left: 0; right: 0; bottom: 0;
    height: 12px;
    display: flex;
  }
  .edge-stripe span { flex: 1; }
  .edge-stripe .green { background: var(--brand-green); }
  .edge-stripe .blue { background: var(--brand-blue); }
</style>
</head>
<body>
  <section class="card card-back" aria-label="Card back">
    <div class="back-pattern" role="img" aria-label="Green leaf illustration with faint leaf shapes over the dark background"></div>
    <div class="back-content">
      <div class="brand">
        <span class="brand-dot"></span>
        <span class="brand-name">Tidal Prime Voltage Collective</span>
      </div>
      <p class="tagline">Reducing your carbon footprint &amp; energy bill at the same time!</p>
    </div>
  </section>

  <section class="card card-front" aria-label="Card front">
    <div class="front-top">
      <div class="brand">
        <span class="brand-dot"></span>
        <span class="brand-name">Tidal Prime Voltage Collective</span>
      </div>
    </div>
    <div class="front-bottom">
      <div class="person">
        <p class="person-name">Gus Marwick</p>
        <p class="person-title">Energy Warrior</p>
        <p class="person-address">47 Orchard Lane Toronto Ontario K4P 2Z7</p>
      </div>
      <ul class="contact-list">
        <li><span class="contact-label label-green">P:</span>(555) 314-2768</li>
        <li><span class="contact-label label-green">F:</span>(555) 862-4091</li>
        <li><span class="contact-label label-green">E:</span>gus@tidalprimevoltage.example</li>
        <li><span class="contact-label label-blue">W:</span>www.tidalprimevoltage.example</li>
      </ul>
    </div>
    <div class="edge-stripe">
      <span class="green"></span><span class="blue"></span><span class="green"></span><span class="blue"></span><span class="green"></span>
    </div>
  </section>
</body>
</html>
```